Web Design Project

We need the homepage and 7 interior pages designed as described below - design only:

Main Page
We like this template: http://www.layoutbarn.example/demo/52917.html

We also want a login dropdown similar to http://www.vortelle.example

We want the main page to be luxurious and sleek. We are a limo company that is dedicated to good service and creating an experience, and our front page should strongly reflect that. We do not want a very busy front page.

The main page should do primary things:

1. Make Reservations: We really like rideharbor.example for this aspect of the site. That being said, rideharbor is NOT the type of company we are.
2. Inform the customer of our most popular packages and give a sense of our professionalism and luxurious service.
3. There should be an area for a customer login
4. Menu should include the following: Home, Who We Are, Our Fleet, Custom Packages,
Testimonials, Book Your Ride!

For a starting point, we like this template http://www.layoutbarn.example/demo/52917.html

Rather than "start up, integrate, develop" we could have 3 of the more popular packages (or categories of packages). The bottom part would be fine. We could have a chirpline feed, welcome, and our core principles. The one big change would be the addition of a "booking" area right smack in the middle of the page, where a customer could enter in trip data and see if the date was available.

-

About Us - Secondary Page
We like this ABOUT page template: http://www.layoutbarn.example/demo/63824.html

This is a really important page that people overlook, yet it is the most viewed page of a website after the homepage. We have come up with a bit of text to go on the about us page:

Who We Are: Velvet Cars was founded on the core principle that every limo ride starts with personalized service from the instant you book your ride and continues after you step out of the car. You and your party are more than just our customers. We consider knowing your name and providing you with your choice of snacks and periodicals in the car just a few of the integral elements of the limousine experience. We are striving to revolutionize the limousine industry by creating a personal, friendly, timely, and professional experience. Velvet Cars combines current technology and a modern fleet with good old-fashioned service to deliver you a personalized, luxury experience. We cater to every event, from business travel to proms and wedding, and everything in between.

We do all of this while maintaining competitive pricing to our peers.

Have a taste of high society...

-

Custom Packages - Secondary Page

This page will contain descriptions of the packages that we offer: Wedding, Prom, Business, etc. - there should be a thumbnail of each package with a description next to it. When you click on a thumbnail it will bring you to a detailed page of that particular package.

-

Custom Packages Interior Page - Secondary Page

In depth look at that particular package - for example, weddings - shows that we offer complimentary champagne, Just married sign, etc.

-

Fleet Page - Secondary Page

This page can be fairly basic. It will include photos of the vehicles along with descriptions and number of passengers, etc.

-

Testimonials Page - Secondary Page

This page will have testimonials from customers. We don't want a big block of text, but rather small testimonials that will expand within the page when you click on a "+" symbol. We like the way it looks when the testimonials are enclosed within a speech bubble image - still professional and classy, not cheesy.

-

Book your ride! - Secondary Page

This page will have a form on it - the same as the form on the homepage, where people can enter in information to check the availability of vehicles. We also want basic contact information on this page as well in case people want to call directly or e-mail.

Requirements
Must have
• - Book your reservation form on homepage
- Sleek, elegant feel
- Chirpline feed

```html
<!DOCTYPE html>
<html lang="en">
<head>
<meta charset="utf-8">
<title>VelvetCars</title>
<link href="https://fonts.googleapis.com/css2?family=Yanone+Kaffeesatz:wght@300;400&family=Open+Sans:ital,wght@0,400;0,600;1,400&display=swap" rel="stylesheet">
<style>
:root{
  --navy-deep:#0b1f4d;
  --navy:#1a3f86;
  --nav-bg:#111418;
  --orange:#c85a10;
  --panel:#4b4b4b;
  --panel-dark:#3a3a3a;
  --paper:#e6e6e6;
  --white:#ffffff;
  --ink:#2d2d2d;
  --muted:#8a8a8a;
  --link-blue:#2e63ad;
  --feed-blue:#2b9bd6;
  --rule:#d4d4d4;
}
*{box-sizing:border-box;margin:0;padding:0}
html,body{width:726px;height:1200px;overflow:hidden}
body{position:relative;background:var(--paper);font-family:"Open Sans",Arial,sans-serif;color:var(--ink)}
.abs{position:absolute}

/* header */
.masthead{left:0;top:0;width:726px;height:400px;
  background:radial-gradient(ellipse 420px 220px at 360px 0,#2c5fb0 0%,var(--navy) 40%,var(--navy-deep) 100%)}
.wordmark{font-family:"Yanone Kaffeesatz",sans-serif;font-weight:400;line-height:1}
.brand{left:92px;top:22px;font-size:26px;color:var(--white)}
.main-nav{left:90px;top:67px;width:542px;height:30px;background:var(--nav-bg)}
.main-nav a{position:absolute;top:0;line-height:30px;font-family:"Yanone Kaffeesatz",sans-serif;font-weight:300;font-size:13px;color:#e6e6e6;text-decoration:none}
.main-nav .login{left:451px;width:91px;height:30px;background:var(--orange);text-align:center;color:#fff;font-weight:400}

/* booking */
.booking{left:90px;top:114px;width:183px;height:263px;background:var(--panel);border-radius:2px;color:#fff}
.booking h2{font-family:"Yanone Kaffeesatz",sans-serif;font-weight:300;font-size:24px;text-align:center;margin-top:8px;color:#e8e8e8}
.trip-tabs{position:absolute;left:9px;top:43px;width:165px;height:21px;background:var(--panel-dark);border-radius:2px;font-size:6px;display:flex;align-items:center}
.trip-tabs span{display:flex;align-items:center;margin-left:6px}
.trip-tabs i{width:6px;height:6px;border-radius:50%;background:#ddd;margin-right:3px;display:inline-block}
.trip-tabs .active{position:absolute;right:0;top:0;height:21px;width:63px;background:#2d2d2d;color:#f08a3a;margin:0;justify-content:center}
.field-label{position:absolute;width:183px;text-align:center;font-size:7.5px;letter-spacing:.5px;font-weight:600}
.input{position:absolute;left:9px;width:165px;height:18px;background:#fff;border:1px solid #ccc;color:#999;font-size:7.5px;padding:4px 5px}
.small-label{position:absolute;font-size:7.5px;font-weight:600}
.select{position:absolute;height:18px;background:#fff;border:1px solid #ccc;color:#555;font-size:7.5px;padding:4px 4px}
.select svg{position:absolute;right:4px;top:6px}
.calc-btn{left:37px;top:214px;width:109px;height:30px;background:linear-gradient(#3f8ae0,#1f5faf);border-radius:3px;font-family:"Yanone Kaffeesatz",sans-serif;font-weight:300;font-size:18px;text-align:center;line-height:30px;color:#fff}

/* hero */
.hero{left:296px;top:114px;width:336px;height:263px;border:2px solid #dcdcdc;border-radius:2px;overflow:hidden;
  background:linear-gradient(100deg,#f2f2f2 0%,#cfcfcf 30%,#4a4a4a 60%,#2b2b2b 100%)}
.hero-quote{left:135px;top:86px;width:178px;font-family:"Yanone Kaffeesatz",sans-serif;font-weight:300;font-size:21px;line-height:27px;color:#fff}
.dots{right:10px;bottom:14px;display:flex;gap:2px}
.dots i{width:5px;height:5px;border-radius:50%;background:#fff;display:block}
.dots i:first-child{background:var(--orange)}

/* content */
.section-title{font-family:"Yanone Kaffeesatz",sans-serif;font-weight:300;color:#444}
.section-title em{font-style:normal;color:var(--link-blue)}
.welcome-title{left:90px;top:406px;font-size:22px}
.welcome-title em{font-size:31px}
.lede{left:90px;width:544px;font-size:7.9px;line-height:14px;color:#333}
.read-more{left:583px;top:530px;width:49px;height:18px;background:linear-gradient(#fff,#e2e2e2);border:1px solid #cfcfcf;border-radius:2px;font-family:"Yanone Kaffeesatz",sans-serif;font-size:9px;color:var(--link-blue);line-height:16px;text-align:center}
.principles-title{left:90px;top:561px;font-size:21px}
.principles{left:90px;top:597px;width:542px;height:339px;background:#fff}
.principle{position:absolute;left:12px;width:518px;height:85px;border-bottom:1px solid var(--rule)}
.principle:last-child{border-bottom:none}
.num{position:absolute;left:0;top:10px;width:22px;height:22px;border-radius:50%;background:linear-gradient(#fff,#e8e8e8);box-shadow:0 1px 2px rgba(0,0,0,.35);font-family:"Yanone Kaffeesatz",sans-serif;font-size:14px;text-align:center;line-height:22px;color:#555}
.principle h3{position:absolute;left:29px;top:11px;font-family:"Yanone Kaffeesatz",sans-serif;font-weight:300;font-size:16px;color:var(--link-blue)}
.principle p{position:absolute;left:0;top:38px;width:518px;font-size:6.8px;line-height:11.5px;color:#333}

/* feed */
.feed-bird{left:226px;top:950px;width:46px;height:38px;border-radius:50%;background:radial-gradient(circle at 40% 55%,#5cc3ee,#2b8fc8)}
.feed-title{left:281px;top:953px;font-size:26px;color:var(--feed-blue)}
.post{position:absolute;width:168px;height:52px}
.avatar{position:absolute;left:0;top:0;width:26px;height:26px;background:#fff;border:1px solid #ccc;padding:2px}
.avatar span{display:block;width:100%;height:100%;background:linear-gradient(#5b8ed6,#c23a2a)}
.avatar.grey span{background:linear-gradient(#999,#333)}
.bubble{position:absolute;left:36px;top:0;width:131px;height:36px;background:#fff;border:1px solid #d6d6d6;border-radius:3px;font-size:6px;font-style:italic;line-height:9px;color:#666;padding:3px 6px}
.bubble a{color:var(--link-blue);font-weight:600;text-decoration:none}
.when{position:absolute;right:0;top:40px;font-size:5.8px;font-style:italic;color:#888}

/* footer */
.footer-rule{left:90px;top:1137px;width:542px;height:1px;background:#c9c9c9}
.copyright{left:90px;top:1146px;font-size:6px;color:#888}
.social{left:90px;top:1162px;display:flex;gap:3px}
.social i{display:block;width:9px;height:9px;border-radius:1px;background:#5a7fb8}
.foot-brand{right:94px;top:1156px;font-size:22px;color:var(--muted)}
</style>
</head>
<body>

<header class="abs masthead">
  <div class="abs brand wordmark">VelvetCars</div>

  <nav class="abs main-nav">
    <a href="#" style="left:12px">HOME</a>
    <a href="#" style="left:55px">WHO WE ARE</a>
    <a href="#" style="left:123px">OUR FLEET</a>
    <a href="#" style="left:182px">CUSTOM PACKAGES</a>
    <a href="#" style="left:270px">TESTIMONIALS</a>
    <a href="#" style="left:342px">BOOK YOUR RIDE!</a>
    <a href="#" class="login">CUSTOMER LOGIN</a>
  </nav>

  <form class="abs booking">
    <h2>BOOK YOUR RIDE NOW</h2>
    <div class="trip-tabs">
      <span><i></i>One Way</span>
      <span><i></i>By The Hour</span>
      <span class="active">Multiple Rides ▸</span>
    </div>
    <div class="field-label" style="top:76px">I WANT TO BE PICKED UP AT:</div>
    <div class="input" style="top:91px">Enter Address, Airport or Landmark:</div>
    <div class="field-label" style="top:119px">...AND DROPPED OFF AT:</div>
    <div class="input" style="top:134px">Enter Address, Airport or Landmark:</div>
    <div class="small-label" style="left:9px;top:163px">Pickup Date:</div>
    <div class="small-label" style="left:106px;top:163px">Pickup Time:</div>
    <div class="select" style="left:10px;top:178px;width:65px">10/6/2012
      <svg width="7" height="7" viewBox="0 0 7 7" style="top:5px"><rect x=".5" y="1" width="6" height="5.5" fill="none" stroke="#c0392b"/><rect x=".5" y="1" width="6" height="1.5" fill="#c0392b"/></svg>
    </div>
    <div class="select" style="left:96px;top:178px;width:41px">9 PM
      <svg width="7" height="4" viewBox="0 0 7 4"><path d="M0 0h7L3.5 4z" fill="#666"/></svg>
    </div>
    <div class="select" style="left:141px;top:178px;width:33px">:30
      <svg width="7" height="4" viewBox="0 0 7 4"><path d="M0 0h7L3.5 4z" fill="#666"/></svg>
    </div>
    <div class="abs calc-btn">CALCUTE PRICE</div>
  </form>

  <section class="abs hero" role="img" aria-label="Photo of a smiling chauffeur in shirt and tie with arms crossed, a suited driver beside a black limousine behind him">
    <p class="abs hero-quote">"Neque porro quisquam qui dolorem ipsum dolor sit amet, adip velit..."</p>
    <div class="abs dots"><i></i><i></i><i></i><i></i><i></i><i></i></div>
  </section>
</header>

<main>
  <h1 class="abs section-title welcome-title">Welcome to <em>VelvetCars</em></h1>
  <p class="abs lede" style="top:448px">Lorem Ipsum is simply dummy text of the printing and typesetting industry. Lorem Ipsum has been the industry's standard dummy text ever since the 1500s, when an unknown printer took a galley of type and scrambled it to make a type specimen book.</p>
  <p class="abs lede" style="top:490px">It has survived not only five centuries, but also the leap into electronic typesetting, remaining essentially unchanged. It was popularised in the 1960s with the release of Letraset sheets containing Lorem Ipsum passages, and more recently with desktop...</p>
  <a class="abs read-more">READ MORE ▸</a>

  <h2 class="abs section-title principles-title">Our <em>Core Principles</em></h2>
  <section class="abs principles">
    <article class="principle" style="top:0">
      <span class="num">1</span>
      <h3>Neque porro quisquam est qui dolorem ipsum quia dolor sit amet</h3>
      <p>Lorem Ipsum is simply dummy text of the printing and typesetting industry. Lorem Ipsum has been the industry's standard dummy text ever since the 1500s, when an unknown printer took a galley of type and scrambled it to make a type specimen book. It has survived not only five centuries, but also the leap into electronic typesetting, remaining essentially unchanged.</p>
    </article>
    <article class="principle" style="top:85px">
      <span class="num">2</span>
      <h3>Neque porro quisquam eipsum quia dolor sit amet</h3>
      <p>Lorem Ipsum is simply dummy text of the printing and typesetting industry. Lorem Ipsum has been the industry's standard dummy text ever since the 1500s, when an unknown printer took a galley of type and scrambled it to make a type specimen book. It has survived not only five centuries, but also the leap into electronic typesetting, remaining essentially unchanged.</p>
    </article>
    <article class="principle" style="top:170px">
      <span class="num">3</span>
      <h3>Neque porro quisquam est qui dolorem ipsum quia dolor sit amet</h3>
      <p>Lorem Ipsum is simply dummy text of the printing and typesetting industry. Lorem Ipsum has been the industry's standard dummy text ever since the 1500s, when an unknown printer took a galley of type and scrambled it to make a type specimen book. It has survived not only five centuries, but also the leap into electronic typesetting, remaining essentially unchanged.</p>
    </article>
    <article class="principle" style="top:255px">
      <span class="num">4</span>
      <h3>Neque porro quisquam eipsum quia dolor sit amet</h3>
      <p>Lorem Ipsum is simply dummy text of the printing and typesetting industry. Lorem Ipsum has been the industry's standard dummy text ever since the 1500s, when an unknown printer took a galley of type and scrambled it to make a type specimen book. It has survived not only five centuries, but also the leap into electronic typesetting, remaining essentially unchanged.</p>
    </article>
  </section>

  <div class="abs feed-bird" role="img" aria-label="Small cartoon bird with a speech bubble"></div>
  <h2 class="abs section-title feed-title">From Chirpline Blogs</h2>

  <section class="feed">
    <div class="post" style="left:90px;top:1007px"><div class="avatar"><span></span></div><p class="bubble">Lorem Ipsum is simply dummy text of the printing and typesetting industry. Lorem Ip <a>http://cl.example/RmNVZNvf</a></p><span class="when">1 hour ago</span></div>
    <div class="post" style="left:277px;top:1007px"><div class="avatar grey"><span></span></div><p class="bubble">Lorem Ipsum is simply dummy text of the printing and typesetting industry. Lorem Ip <a>http://cl.example/RmNVZNvf</a></p><span class="when">1 hour ago</span></div>
    <div class="post" style="left:464px;top:1007px"><div class="avatar"><span></span></div><p class="bubble">Lorem Ipsum is simply dummy text of the printing and typesetting industry. Lorem Ip <a>http://cl.example/RmNVZNvf</a></p><span class="when">1 hour ago</span></div>
    <div class="post" style="left:90px;top:1063px"><div class="avatar"><span></span></div><p class="bubble">Lorem Ipsum is simply dummy text of the printing and typesetting industry. Lorem Ip <a>http://cl.example/RmNVZNvf</a></p><span class="when">1 hour ago</span></div>
    <div class="post" style="left:277px;top:1063px"><div class="avatar grey"><span></span></div><p class="bubble">Lorem Ipsum is simply dummy text of the printing and typesetting industry. Lorem Ip <a>http://cl.example/RmNVZNvf</a></p><span class="when">1 hour ago</span></div>
    <div class="post" style="left:464px;top:1063px"><div class="avatar"><span></span></div><p class="bubble">Lorem Ipsum is simply dummy text of the printing and typesetting industry. Lorem Ip <a>http://cl.example/RmNVZNvf</a></p><span class="when">1 hour ago</span></div>
  </section>
</main>

<footer>
  <div class="abs footer-rule"></div>
  <p class="abs copyright">Copyright © 2012 VelvetCars. All Rights Reserved. &nbsp;|&nbsp; Privacy Policy</p>
  <div class="abs social"><i></i><i></i><i></i></div>
  <div class="abs foot-brand wordmark">VelvetCars</div>
</footer>

</body>
</html>
```